Schema Paladin Powerpoint with Commander Ravelle Type Theme

Need powerpoint template with matching colors and different slide options. Logo and colors to be used can be found at schemapaladinhq.com. Want brightly colored slide deck that is readable form the back of a room, but highlights colors. I will be incorporating Trivano into the slides to gamify my presentations.

Target Market(s)

Tech

Industry/Entity Type

IT, specifically database, but crossing over to mental health in IT, important note this is not for a company, this is just for a professional building a brand

Font styles to use
Sans Serif

Colors
0054AA
0677BA
7BADD7
CADEEF
E8F1F8
EB3D1F
EC4F4E
F09395
F8D3D4
FCEDEE

Requirements
Must have
• My Logo in the bottom corner, front page, a thank your page, question page, content page, content page with two columns, content page with graphs, and icons to be used in the primary colors of the logos, About Me Page, Break Slides, Demo break slide
Should not have
• Lighter shades of colors, I want to pop out where colors are used, I want spacing and font size to be readable from the back of a room, most likely black text and white background

```html
<!DOCTYPE html>
<html lang="en">
<head>
<meta charset="utf-8">
<title>Schema Paladin – Presentation Template</title>
<link href="https://fonts.googleapis.com/css2?family=Krona+One&family=Arimo:wght@400;700&display=swap" rel="stylesheet">
<style>
  :root {
    --navy: #183f7d;
    --red: #e8192a;
    --blue: #0f7ac0;
    --ink: #333333;
    --muted: #555555;
    --grid: #d9d9d9;
    --page: #c4c4c4;
    --white: #ffffff;
  }
  * { box-sizing: border-box; margin: 0; padding: 0; }
  html, body { width: 1200px; height: 3320px; overflow: hidden; }
  body { background: var(--page); font-family: "Arimo", Arial, sans-serif; position: relative; }

  .slide { position: absolute; left: 88px; width: 1025px; height: 576px; background: var(--white); overflow: hidden; }
  .slide--cover { top: 71px; background: var(--navy); }
  .slide--about { top: 722px; }
  .slide--columns { top: 1371px; }
  .slide--questions { top: 2021px; }
  .slide--chart { top: 2671px; }

  .slide-header { position: absolute; left: 0; top: 0; width: 1025px; height: 78px; }
  .slide-title { position: absolute; left: 63px; top: 14px; font-family: "Krona One", "Arial Black", sans-serif; font-size: 26px; color: var(--white); letter-spacing: 1px; }

  .slide-footer { position: absolute; left: 0; bottom: 0; width: 1025px; height: 24px; }
  .footer-page { position: absolute; left: 63px; bottom: 6px; font-size: 10.5px; font-weight: 700; color: var(--white); }
  .footer-copy { position: absolute; left: 0; width: 1024px; text-align: center; bottom: 6px; font-size: 10.5px; color: var(--white); }
  .footer-brand { position: absolute; right: 46px; bottom: 8px; display: flex; align-items: center; gap: 6px; font-family: "Krona One", sans-serif; font-size: 10px; color: var(--navy); }
  .footer-brand .mark { width: 22px; height: 22px; border-radius: 50%; background: var(--navy); }

  /* Cover */
  .cover-art { position: absolute; left: 0; top: 0; }
  .cover-title { position: absolute; left: 61px; top: 122px; font-family: "Krona One", "Arial Black", sans-serif; font-size: 44px; line-height: 52px; color: var(--white); letter-spacing: 1px; }
  .cover-intro { position: absolute; left: 61px; top: 243px; width: 430px; font-size: 13px; line-height: 24px; font-weight: 700; color: var(--white); }
  .cover-photo { position: absolute; left: 540px; top: 60px; width: 440px; height: 320px; border-radius: 40% 40% 45% 45% / 30% 30% 60% 60%; background: radial-gradient(circle at 50% 40%, #b8977a 0%, #6f6a72 45%, #2c4f86 100%); }
  .cover-brand { position: absolute; left: 0; width: 1025px; top: 482px; display: flex; justify-content: center; align-items: center; gap: 12px; font-family: "Krona One", sans-serif; font-size: 24px; color: var(--navy); }
  .cover-brand .mark { width: 56px; height: 56px; border-radius: 50%; background: var(--navy); }

  /* About */
  .about-text { position: absolute; left: 63px; top: 124px; width: 422px; font-size: 11.3px; line-height: 23.5px; color: var(--muted); text-align: justify; }
  .about-text p + p { margin-top: 15px; }
  .about-photo { position: absolute; left: 514px; top: 129px; width: 511px; height: 367px; clip-path: polygon(70px 0, 100% 0, 100% 100%, 0 100%); background: linear-gradient(100deg, #3d4a63 0%, #5d6f8e 35%, #1f4f86 65%, #0f2b55 100%); }

  /* Two columns */
  .columns { position: absolute; top: 142px; left: 63px; width: 900px; display: flex; gap: 57px; }
  .columns .col { width: 422px; font-size: 11.3px; line-height: 23.5px; color: var(--muted); }
  .columns .col p:first-child { text-align: left; }
  .columns .col p + p { margin-top: 15px; text-align: justify; }

  /* Questions */
  .qa { position: absolute; display: flex; align-items: center; gap: 12px; width: 400px; }
  .qa .badge { flex: none; width: 33px; height: 33px; border-radius: 50%; color: var(--white); font-weight: 700; font-size: 13px; display: flex; align-items: center; justify-content: center; border: 3px solid var(--white); box-shadow: 0 2px 5px rgba(0,0,0,.3); }
  .qa--q .badge { background: var(--navy); }
  .qa--a .badge { background: var(--red); }
  .qa .text { font-size: 13px; line-height: 18.5px; font-weight: 700; }
  .qa--q .text { color: var(--muted); }
  .qa--a .text { color: #111111; }

  /* Chart */
  .chart { position: absolute; left: 40px; top: 118px; }
  .chart text { font-family: "Arimo", Arial, sans-serif; font-size: 12px; font-weight: 700; fill: var(--ink); }
  .checklist { position: absolute; left: 683px; top: 130px; width: 290px; list-style: none; }
  .checklist li { position: relative; padding-left: 22px; font-size: 12.5px; line-height: 20px; color: var(--muted); margin-bottom: 10px; }
  .checklist li svg { position: absolute; left: 0; top: 3px; }
</style>
</head>
<body>

<!-- Cover -->
<section class="slide slide--cover">
  <svg class="cover-art" width="1025" height="576" viewBox="0 0 1025 576" aria-hidden="true">
    <path d="M0,488 Q512,330 1025,488 L1025,576 L0,576 Z" fill="var(--red)"/>
    <path d="M0,500 Q512,372 1025,500 L1025,576 L0,576 Z" fill="var(--white)"/>
  </svg>
  <h1 class="cover-title">SCHEMA<br>PALADIN</h1>
  <p class="cover-intro">Marla Quenneth is currently a Data Platform Champion, DataSpark 2020 Award winner, and works as a Senior Database Administrator for Ledgerwise.</p>
  <div class="cover-photo" role="img" aria-label="Photo of a woman working on a laptop, framed in a shield shape"></div>
  <div class="cover-brand"><span class="mark"></span><span>Schema Paladin</span></div>
</section>

<!-- About me -->
<section class="slide slide--about">
  <svg class="slide-header" viewBox="0 0 1025 78" aria-hidden="true">
    <polygon points="0,0 869,0 834,62 0,62" fill="var(--navy)"/>
    <polygon points="878,0 1025,0 1025,62 843,62" fill="var(--red)"/>
    <polygon points="0,62 632,62 624,78 0,78" fill="var(--blue)"/>
  </svg>
  <h2 class="slide-title">YOUR TITLE HERE</h2>
  <div class="about-text">
    <p>Marla Quenneth is currently a Data Platform Champion, DataSpark 2020 Award winner, and works as a Senior Database Administrator for Ledgerwise. Marla has worked on RelaQL Engine since 6.5. She is currently a co-leader of the Triangle Data User Group in Raleigh, NC and Inclusion Virtual Group. Marla tinkered with databases in middle school to keep her sports card collection organized and got an early start on databases.</p>
    <p>When not doing things in the Data Platform community she likes to be somewhere making a difference. Her passion outside of RelaQL Engine is volunteering by advocating for abused and neglected foster children in court through the Harbor Voices Child Advocate program. This is her favorite and most important job. She has been a child advocate for since 2003 and advocated for over 60 children. As someone who experienced mental health issues she has for the past two years started being a mental health advocate by being a part of the MIRA (Mental Illness Rights and Advocacy) Advisory Council with the ARA (Access Rights Alliance).</p>
  </div>
  <div class="about-photo" role="img" aria-label="Photo of a man with a laptop standing beside server racks"></div>
  <svg class="slide-footer" viewBox="0 0 1025 24" aria-hidden="true"><polygon points="0,0 802,0 818,24 0,24" fill="var(--red)"/></svg>
  <span class="footer-page">PAGE | 02</span>
  <span class="footer-copy">© 2021 Company Name | All Rights Reserved</span>
  <div class="footer-brand"><span class="mark"></span><span>Schema Paladin</span></div>
</section>

<!-- Two columns -->
<section class="slide slide--columns">
  <svg class="slide-header" viewBox="0 0 1025 78" aria-hidden="true">
    <polygon points="0,0 869,0 834,62 0,62" fill="var(--navy)"/>
    <polygon points="878,0 1025,0 1025,62 843,62" fill="var(--red)"/>
    <polygon points="0,62 632,62 624,78 0,78" fill="var(--blue)"/>
  </svg>
  <h2 class="slide-title">YOUR TITLE HERE</h2>
  <div class="columns">
    <div class="col">
      <p>Lorem ipsum dolor sit amet, consectetur adipiscing elit, sed do eiusmod tempor incididunt ut labore et dolore magna aliqua. Ut enim ad minim veniam, quis nostrud exercitation ullamco laboris nisi ut aliquip ex ea commodo consequat. Duis aute irure dolor in reprehenderit in voluptate velit esse cillum dolore eu fugiat nulla pariatur. Excepteur sint occaecat cupidatat non proident, sunt in culpa qui officia deserunt mollit anim id est laborum.</p>
      <p>Sed ut perspiciatis unde omnis iste natus error sit voluptatem accusantium doloremque laudantium, totam rem aperiam, eaque ipsa quae ab illo inventore veritatis et quasi architecto beatae vitae dicta sunt explicabo. Nemo enim ipsam voluptatem quia voluptas sit aspernatur aut odit aut fugit, sed quia consequuntur magni dolores eos qui ratione voluptatem sequi nesciunt. Neque porro quisquam est, qui dolorem ipsum quia dolor sit amet, consectetur, adipisci velit, sed quia non numquam eius modi tempora incidunt ut labore et dolore magnam aliquam quaerat voluptatem.</p>
    </div>
    <div class="col">
      <p>Lorem ipsum dolor sit amet, consectetur adipiscing elit, sed do eiusmod tempor incididunt ut labore et dolore magna aliqua. Ut enim ad minim veniam, quis nostrud exercitation ullamco laboris nisi ut aliquip ex ea commodo consequat. Duis aute irure dolor in reprehenderit in voluptate velit esse cillum dolore eu fugiat nulla pariatur. Excepteur sint occaecat cupidatat non proident, sunt in culpa qui officia deserunt mollit anim id est laborum.</p>
      <p>Sed ut perspiciatis unde omnis iste natus error sit voluptatem accusantium doloremque laudantium, totam rem aperiam, eaque ipsa quae ab illo inventore veritatis et quasi architecto beatae vitae dicta sunt explicabo. Nemo enim ipsam voluptatem quia voluptas sit aspernatur aut odit aut fugit, sed quia consequuntur magni dolores eos qui ratione voluptatem sequi nesciunt. Neque porro quisquam est, qui dolorem ipsum quia dolor sit amet, consectetur, adipisci velit, sed quia non numquam eius modi tempora incidunt ut labore et dolore magnam aliquam quaerat voluptatem.</p>
    </div>
  </div>
  <svg class="slide-footer" viewBox="0 0 1025 24" aria-hidden="true"><polygon points="0,0 802,0 818,24 0,24" fill="var(--red)"/></svg>
  <span class="footer-page">PAGE | 03</span>
  <span class="footer-copy">© 2021 Company Name | All Rights Reserved</span>
  <div class="footer-brand"><span class="mark"></span><span>Schema Paladin</span></div>
</section>

<!-- Questions -->
<section class="slide slide--questions">
  <svg class="slide-header" viewBox="0 0 1025 78" aria-hidden="true">
    <polygon points="0,0 869,0 834,62 0,62" fill="var(--navy)"/>
    <polygon points="878,0 1025,0 1025,62 843,62" fill="var(--red)"/>
    <polygon points="0,62 632,62 624,78 0,78" fill="var(--blue)"/>
  </svg>
  <h2 class="slide-title">YOUR TITLE HERE</h2>

  <div class="qa qa--q" style="left:94px;top:128px"><span class="badge">Q</span><span class="text">Lorem ipsum dolor sit amet, consectetur adipiscing elit, sed do eiusmod tempor incididunt</span></div>
  <div class="qa qa--a" style="left:94px;top:183px"><span class="badge">Q</span><span class="text">Lorem ipsum dolor sit amet, consectetur adipiscing elit, sed do eiusmod tempor incididunt</span></div>
  <div class="qa qa--q" style="left:94px;top:264px"><span class="badge">Q</span><span class="text">Lorem ipsum dolor sit amet, consectetur adipiscing elit, sed do eiusmod tempor incididunt</span></div>
  <div class="qa qa--a" style="left:94px;top:320px"><span class="badge">Q</span><span class="text">Lorem ipsum dolor sit amet, consectetur adipiscing elit, sed do eiusmod tempor incididunt</span></div>
  <div class="qa qa--q" style="left:94px;top:401px"><span class="badge">Q</span><span class="text">Lorem ipsum dolor sit amet, consectetur adipiscing elit, sed do eiusmod tempor incididunt</span></div>
  <div class="qa qa--a" style="left:94px;top:456px"><span class="badge">Q</span><span class="text">Lorem ipsum dolor sit amet, consectetur adipiscing elit, sed do eiusmod tempor incididunt</span></div>

  <div class="qa qa--q" style="left:544px;top:128px"><span class="badge">Q</span><span class="text">Lorem ipsum dolor sit amet, consectetur adipiscing elit, sed do eiusmod tempor incididunt</span></div>
  <div class="qa qa--a" style="left:544px;top:183px"><span class="badge">Q</span><span class="text">Lorem ipsum dolor sit amet, consectetur adipiscing elit, sed do eiusmod tempor incididunt</span></div>
  <div class="qa qa--q" style="left:544px;top:264px"><span class="badge">Q</span><span class="text">Lorem ipsum dolor sit amet, consectetur adipiscing elit, sed do eiusmod tempor incididunt</span></div>
  <div class="qa qa--a" style="left:544px;top:320px"><span class="badge">Q</span><span class="text">Lorem ipsum dolor sit amet, consectetur adipiscing elit, sed do eiusmod tempor incididunt</span></div>
  <div class="qa qa--q" style="left:544px;top:401px"><span class="badge">Q</span><span class="text">Lorem ipsum dolor sit amet, consectetur adipiscing elit, sed do eiusmod tempor incididunt</span></div>
  <div class="qa qa--a" style="left:544px;top:456px"><span class="badge">Q</span><span class="text">Lorem ipsum dolor sit amet, consectetur adipiscing elit, sed do eiusmod tempor incididunt</span></div>

  <svg class="slide-footer" viewBox="0 0 1025 24" aria-hidden="true"><polygon points="0,0 802,0 818,24 0,24" fill="var(--red)"/></svg>
  <span class="footer-page">PAGE | 04</span>
  <span class="footer-copy">© 2021 Company Name | All Rights Reserved</span>
  <div class="footer-brand"><span class="mark"></span><span>Schema Paladin</span></div>
</section>

<!-- Chart -->
<section class="slide slide--chart">
  <svg class="slide-header" viewBox="0 0 1025 78" aria-hidden="true">
    <polygon points="0,0 869,0 834,62 0,62" fill="var(--navy)"/>
    <polygon points="878,0 1025,0 1025,62 843,62" fill="var(--red)"/>
    <polygon points="0,62 632,62 624,78 0,78" fill="var(--blue)"/>
  </svg>
  <h2 class="slide-title">YOUR TITLE HERE</h2>

  <svg class="chart" width="600" height="380" viewBox="0 0 600 380" role="img" aria-label="Bar chart of two series across the week">
    <!-- plot: x 43..590, y 10 (120) .. 350 (0) -->
    <g stroke="var(--grid)" stroke-width="1">
      <line x1="43" y1="10" x2="590" y2="10"/>
      <line x1="43" y1="10" x2="43" y2="350"/>
      <line x1="121" y1="10" x2="121" y2="350"/>
      <line x1="199" y1="10" x2="199" y2="350"/>
      <line x1="277" y1="10" x2="277" y2="350"/>
      <line x1="355" y1="10" x2="355" y2="350"/>
      <line x1="433" y1="10" x2="433" y2="350"/>
      <line x1="511" y1="10" x2="511" y2="350"/>
      <line x1="590" y1="10" x2="590" y2="350"/>
      <line x1="43" y1="350" x2="590" y2="350"/>
    </g>
    <g text-anchor="end">
      <text x="22" y="14">120</text>
      <text x="22" y="71">100</text>
      <text x="22" y="127">80</text>
      <text x="22" y="184">60</text>
      <text x="22" y="241">40</text>
      <text x="22" y="297">20</text>
      <text x="22" y="354">0</text>
    </g>
    <!-- bars: height = value * 2.833 -->
    <g fill="var(--red)">
      <rect x="67" y="67" width="14" height="283"/>
      <rect x="145" y="95" width="14" height="255"/>
      <rect x="223" y="208" width="14" height="142"/>
      <rect x="301" y="67" width="14" height="283"/>
      <rect x="379" y="67" width="14" height="283"/>
      <rect x="457" y="180" width="14" height="170"/>
      <rect x="535" y="208" width="14" height="142"/>
    </g>
    <g fill="var(--navy)">
      <rect x="90" y="95" width="14" height="255"/>
      <rect x="168" y="123" width="14" height="227"/>
      <rect x="246" y="67" width="14" height="283"/>
      <rect x="324" y="180" width="14" height="170"/>
      <rect x="402" y="95" width="14" height="255"/>
      <rect x="480" y="138" width="14" height="212"/>
      <rect x="558" y="67" width="14" height="283"/>
    </g>
    <g text-anchor="middle">
      <text x="74" y="60">100</text><text x="97" y="88">90</text>
      <text x="152" y="88">90</text><text x="175" y="116">80</text>
      <text x="230" y="201">50</text><text x="253" y="60">100</text>
      <text x="308" y="60">100</text><text x="331" y="173">60</text>
      <text x="386" y="60">100</text><text x="409" y="88">90</text>
      <text x="464" y="173">60</text><text x="487" y="131">75</text>
      <text x="542" y="201">50</text><text x="565" y="60">100</text>
    </g>
    <g text-anchor="middle">
      <text x="86" y="372">Sun</text>
      <text x="163" y="372">Mon</text>
      <text x="241" y="372">Tue</text>
      <text x="318" y="372">Wed</text>
      <text x="397" y="372">Thu</text>
      <text x="472" y="372">Fri</text>
      <text x="547" y="372">Sat</text>
    </g>
  </svg>

  <ul class="checklist">
    <li><svg width="13" height="13" viewBox="0 0 13 13" aria-hidden="true"><circle cx="6.5" cy="6.5" r="6.5" fill="var(--red)"/><path d="M3.5 6.7 L5.7 8.8 L9.6 4.5" fill="none" stroke="#fff" stroke-width="1.8"/></svg>Lorem ipsum dolor sit consectetur adipiscing elit, sed do eiusmod tempor incididunt ut labore et dolore magna aliqua.</li>
    <li><svg width="13" height="13" viewBox="0 0 13 13" aria-hidden="true"><circle cx="6.5" cy="6.5" r="6.5" fill="var(--red)"/><path d="M3.5 6.7 L5.7 8.8 L9.6 4.5" fill="none" stroke="#fff" stroke-width="1.8"/></svg>Lorem ipsum dolor sit consectetur adipiscing elit, sed do eiusmod</li>
    <li><svg width="13" height="13" viewBox="0 0 13 13" aria-hidden="true"><circle cx="6.5" cy="6.5" r="6.5" fill="var(--red)"/><path d="M3.5 6.7 L5.7 8.8 L9.6 4.5" fill="none" stroke="#fff" stroke-width="1.8"/></svg>Lorem ipsum dolor sit consectetur adipiscing elit, sed do eiusmod tempor incididunt ut labore et dolore magna aliqua.</li>
    <li><svg width="13" height="13" viewBox="0 0 13 13" aria-hidden="true"><circle cx="6.5" cy="6.5" r="6.5" fill="var(--red)"/><path d="M3.5 6.7 L5.7 8.8 L9.6 4.5" fill="none" stroke="#fff" stroke-width="1.8"/></svg>Lorem ipsum dolor sit consectetur adipiscing elit, sed do eiusmod</li>
    <li><svg width="13" height="13" viewBox="0 0 13 13" aria-hidden="true"><circle cx="6.5" cy="6.5" r="6.5" fill="var(--red)"/><path d="M3.5 6.7 L5.7 8.8 L9.6 4.5" fill="none" stroke="#fff" stroke-width="1.8"/></svg>Lorem ipsum dolor sit consectetur adipiscing elit, sed do eiusmod tempor incididunt ut labore et dolore magna aliqua.</li>
    <li><svg width="13" height="13" viewBox="0 0 13 13" aria-hidden="true"><circle cx="6.5" cy="6.5" r="6.5" fill="var(--red)"/><path d="M3.5 6.7 L5.7 8.8 L9.6 4.5" fill="none" stroke="#fff" stroke-width="1.8"/></svg>Lorem ipsum dolor sit consectetur adipiscing elit, sed do eiusmod</li>
  </ul>

  <svg class="slide-footer" viewBox="0 0 1025 24" aria-hidden="true"><polygon points="0,0 802,0 818,24 0,24" fill="var(--red)"/></svg>
  <span class="footer-page">PAGE | 05</span>
  <span class="footer-copy">© 2021 Company Name | All Rights Reserved</span>
  <div class="footer-brand"><span class="mark"></span><span>Schema Paladin</span></div>
</section>

</body>
</html>
```